Internation Biosecurity Business that needs a to design a Label for Itch relief product

Brand Name: Harbor Dermis
I have a logo.
Label sign is 2.5 x 5.5
Label will be printed on clear vinyl.
The bottle to receive this label is colour of white.

I like the look of a label with the bottom starting off as a solid colour and transitioning to white at the top. But if you have something else you would like to try I am going to be open to it.
What ever colours and design you create it must reflect a natural, clean, soothing feeling. This colour could stop on the main panel or continue across to the side panel.
Primary panel size 2.5 x 3, Back side panel size 2.5 x 2.5 for a total size of 2.5 x 5.5 inches
Text on primary panel:
logo (which will have the brand name Harbor Dermis incorporated in it)
- Itch Relief (main message to stand out big ! )
- from Psoriasis, Eczema, Dermatitis (secondary message) but also must stand out but less than "Itch Relief"
- Natural, Nontoxic, Non- medicated (place at bottom
- 100ml (Bottle size)
I am looking for a symbol to be in the background on the main panel or as a water mark on the back panel. This symbol will have a very light outline so it hardly noticed. The symbol I had in mind was the "Harbor Bell" because it stands for freedom. My hope is this will convey a subliminal message of freedom, liberty and trust. You can be free to select a different symbol or nothing at all.

The logo that I have attached Harbor Dermis but these colours must be changed to new colours which must harmonize with the colour you select for the over all label.
I will be coming out with many more labels in this "Harbor" line so the designer that creates the winning art work will be hired in the not-so- distant future for all new labels.
The product is water based and sprayed on. Active ingredient is HOCL. You cannot harm yourself even if it get in your eyes. Our products comes at treating the problems from a Holistic approach and not from a chemical medicated approach.
Company Name: PuraKleen Systems Inc. Box 4087, Innisfail Alberta, T9K 3M2 1 800-517 -2946 Made in Canada (UPC Code: 6 51920 48163 2)

Industry/Entity Type

Business

Colors
886aae
b7a5cd
e4daeb

Requirements
Must have
• Final Graphic files must be in vector/eps format! I need you to enlarge it more because I can not read or see label text or see how you have placed the bell even at the 150%. The situation is that I will be using the winning design as a template for Harbor Peak, Harbor Dermis and Harbor Vita. Each of these categories may have 2 - 4 different products in them. What will distinguished these categories will be a different colour at the bottom of the label. For the Harbor Dermis label I have chosen the mauve or light purple. Light green of Harbor Peak, Light blue for Harbor Vita.
• At the bottom of the label let remove "Antimicrobial Cleanser". One of the problems we Canada's manufacturers have is that some keg words on our labels mush me in French and your present design does not lend itself to incorporating French. We may be able to have a French label underneath the English label, However, The words "Itch Relief" and the phase "Natural, Nontoxic, Non-Medicated" would need to be in French, at a reduced size, so we may need some space. French for Itch Relief is: D mangeaison de secours (place very small under "Itch Relief") French for Natural, Nontoxic, Non-medicated is : Naturel, Non toxque, Non meddicamenteux, place very small under the English.
Should not have
• The same colours that are in the Harbor Dermis Logo. I want different colours.

```html
<!DOCTYPE html>
<html lang="en">
<head>
<meta charset="utf-8">
<title>Harbor Dermis Itch Relief Label</title>
<link rel="stylesheet" href="https://fonts.googleapis.com/css2?family=Open+Sans:wght@400;600;700;800&family=Oswald:wght@300&display=swap">
<style>
  :root {
    --canvas: #ffffff;
    --cream: #fcf7c2;
    --cream-soft: #fffdf0;
    --mauve: #886aae;
    --mauve-deep: #7a5aa3;
    --mauve-light: #b7a5cd;
    --lilac: #e4daeb;
    --plum: #9b1f85;
    --ink: #2a2a2a;
    --body: #3a3a3a;
  }
  * { box-sizing: border-box; margin: 0; padding: 0; }
  html, body { width: 857px; height: 1200px; overflow: hidden; background: var(--canvas); }
  .sheet { position: relative; width: 857px; height: 1200px; }

  .panel { position: absolute; top: 53px; width: 361px; height: 360px; overflow: hidden; }
  .panel--front { left: 59px; }
  .panel--back { left: 437px; }
  .panel__art { position: absolute; inset: 0; width: 100%; height: 100%; }

  .brand { position: absolute; top: 36px; left: 0; right: 0; display: flex; justify-content: center; align-items: center; gap: 8px; }
  .brand__mark { width: 30px; height: 30px; background: var(--mauve-light); }
  .brand__name { font-family: "Open Sans", sans-serif; font-weight: 700; font-size: 24px; color: var(--mauve-deep); line-height: 1; }

  .headline { position: absolute; top: 112px; left: 0; right: 0; text-align: center; font-family: "Open Sans", sans-serif; font-weight: 800; font-size: 45px; letter-spacing: 0.5px; color: var(--plum); line-height: 1; }
  .subhead { position: absolute; top: 166px; left: 0; right: 0; text-align: center; font-family: "Open Sans", sans-serif; font-weight: 600; font-size: 14.5px; color: var(--ink); }

  .claim, .volume { position: absolute; left: 0; right: 0; text-align: center; font-family: "Oswald", sans-serif; font-weight: 300; color: var(--lilac); line-height: 1.2; }
  .claim { top: 270px; font-size: 19px; letter-spacing: 0.3px; }
  .volume { top: 314px; font-size: 19px; }

  .copy { position: absolute; top: 28px; left: 46px; width: 286px; font-family: "Open Sans", sans-serif; font-size: 10.3px; line-height: 15.3px; letter-spacing: -0.25px; color: var(--body); }
  .copy p { margin-bottom: 1px; }
  .copy strong { font-weight: 700; color: var(--ink); }
  .copy .objective { display: grid; grid-template-columns: auto 170px; column-gap: 5px; }

  .ingredients { position: absolute; top: 284px; width: 127px; border-collapse: collapse; font-family: "Open Sans", sans-serif; font-size: 7.6px; letter-spacing: -0.1px; color: #ffffff; }
  .ingredients--en { left: 47px; }
  .ingredients--fr { left: 193px; }
  .ingredients th, .ingredients td { border: 1px solid var(--lilac); padding: 0 3px; text-align: left; font-weight: 400; height: 13px; line-height: 11px; white-space: nowrap; }
  .ingredients th { text-align: center; font-weight: 600; }
  .ingredients td.amount { width: 32px; }
</style>
</head>
<body>
<main class="sheet">

  <section class="panel panel--front" aria-label="Front panel">
    <svg class="panel__art" viewBox="0 0 361 360" preserveAspectRatio="none" aria-hidden="true">
      <defs>
        <linearGradient id="frontSky" x1="0" y1="0" x2="0" y2="1">
          <stop offset="0" stop-color="var(--cream)"/>
          <stop offset="0.55" stop-color="var(--cream-soft)"/>
          <stop offset="1" stop-color="#ffffff"/>
        </linearGradient>
        <linearGradient id="frontBand" x1="0" y1="0" x2="0" y2="1">
          <stop offset="0" stop-color="var(--mauve-light)"/>
          <stop offset="0.3" stop-color="var(--mauve)"/>
          <stop offset="1" stop-color="var(--mauve-deep)"/>
        </linearGradient>
      </defs>
      <rect width="361" height="360" fill="url(#frontSky)"/>
      <path d="M0 214 C60 232 120 240 190 222 C250 206 310 190 361 196 L361 360 L0 360 Z" fill="var(--mauve-light)" opacity="0.7"/>
      <path d="M0 222 C60 238 120 246 190 228 C250 212 310 198 361 203 L361 360 L0 360 Z" fill="url(#frontBand)"/>
    </svg>
    <div class="brand">
      <span class="brand__mark"></span>
      <span class="brand__name">Harbor Dermis</span>
    </div>
    <h1 class="headline">ITCH RELIEF</h1>
    <p class="subhead">from Psoriasis, Eczema, Dermatitis</p>
    <p class="claim">Natural, Nontoxic, Non-Medicated</p>
    <p class="volume">100ml</p>
  </section>

  <section class="panel panel--back" aria-label="Back panel">
    <svg class="panel__art" viewBox="0 0 361 360" preserveAspectRatio="none" aria-hidden="true">
      <defs>
        <linearGradient id="backSky" x1="0" y1="0" x2="0" y2="1">
          <stop offset="0" stop-color="var(--cream)"/>
          <stop offset="0.6" stop-color="var(--cream-soft)"/>
          <stop offset="1" stop-color="#ffffff"/>
        </linearGradient>
        <linearGradient id="backBand" x1="0" y1="0" x2="0" y2="1">
          <stop offset="0" stop-color="var(--mauve-light)"/>
          <stop offset="0.3" stop-color="var(--mauve)"/>
          <stop offset="1" stop-color="var(--mauve-deep)"/>
        </linearGradient>
      </defs>
      <rect width="361" height="360" fill="url(#backSky)"/>
      <path d="M0 262 C60 252 110 232 180 232 C250 232 310 250 361 252 L361 360 L0 360 Z" fill="var(--mauve-light)" opacity="0.7"/>
      <path d="M0 272 C60 260 110 240 180 240 C250 240 310 258 361 260 L361 360 L0 360 Z" fill="url(#backBand)"/>
    </svg>
    <div class="copy">
      <p>Harbor Dermis is a natural, non-toxic, non prescription anti-microbial cleanser.</p>
      <p class="objective"><strong>Objective :</strong><span>To effectively and painlessly provide fast relief.</span></p>
      <p><strong>Directions :</strong> Spray on affected area, repeat 2 – 4 times per day. In severe cases saturate clean bandage with Harbor Dermis Itch Relief and apply overnight. Keeping the area wet with Harbor Dermis will maximize performance. If area does not improve within seven days seek medical advice.</p>
      <p><strong>STORAGE :</strong> Keep bottle sealed and at room temperature for optimum shelf life. Biodegradable.</p>
    </div>
    <table class="ingredients ingredients--en">
      <tr><th colspan="2">INGREDIENTS</th></tr>
      <tr><td>Ionized water</td><td class="amount"></td></tr>
      <tr><td>Hypochlorous acid (HOCL)</td><td class="amount">50mg/L</td></tr>
      <tr><td>Sodium chloride</td><td class="amount">15mg/L</td></tr>
    </table>
    <table class="ingredients ingredients--fr" lang="fr">
      <tr><th colspan="2">INGRÉDIENTS</th></tr>
      <tr><td>Ionisé eau</td><td class="amount"></td></tr>
      <tr><td>L'Acide hypochloreux</td><td class="amount">50mg/L</td></tr>
      <tr><td>Le chlorure de sodium</td><td class="amount">15mg/L</td></tr>
    </table>
  </section>

</main>
</body>
</html>
```